Meridian Swift add on sales tool2017

This will be a flyer to leave with our clients we just did work for. We want to entice them to use our other services over the next 30 days with a discount, money off etc. we will write in the special and the expiration date. I want the client to read the description and see a picture of the service they may want done.

Target Market(s)

Repeat clients

Industry/Entity Type

Cleaning Service

Font styles to use
Serif
Sans Serif

Colors
ec1f27
000000
b1b1b1

Requirements
Must have
• Call to action! look high end market, clients show we do 1st class work.
• Don't Waite
Nice to have
• Classy, quality, I'm open to using other pictures that may look better
Should not have
• Look like a typical carpet cleaners special flyer
• Not to look cluttered

```html
<!DOCTYPE html>
<html lang="en">
<head>
<meta charset="utf-8">
<title>Meridian Swift – Service Flyer</title>
<link rel="stylesheet" href="https://fonts.googleapis.com/css2?family=Arimo:wght@400;700&family=Crimson+Pro:wght@600;700&family=Source+Sans+3:wght@400;700&display=swap">
<style>
  :root {
    --red: #ec1f27;
    --black: #000000;
    --silver: #b1b1b1;
    --stage: #5f5f5f;
    --white: #ffffff;
    --ink: #141414;
    --sans-head: "Arimo", Arial, sans-serif;
    --sans-body: "Source Sans 3", "Segoe UI", sans-serif;
    --serif: "Crimson Pro", Georgia, serif;
  }
  html, body { margin: 0; padding: 0; overflow: hidden; }
  .canvas {
    position: relative; width: 1200px; height: 1200px;
    background: var(--stage); overflow: hidden;
  }
  .page {
    position: absolute; width: 700px; height: 990px;
    background: var(--black); overflow: hidden;
    transform: scale(0.8); transform-origin: 0 0;
  }
  .page--front { left: 28px; top: 204px; }
  .page--back  { left: 612px; top: 204px; }
  .abs { position: absolute; }
  .fill { position: absolute; inset: 0; width: 100%; height: 100%; }

  /* Front: brand */
  .brand-dot { left: 48px; top: 40px; width: 82px; height: 82px; border-radius: 50%; background: var(--red); }
  .brand-name {
    left: 196px; top: 34px; margin: 0;
    font: 700 48px/1 var(--sans-head); color: var(--red); letter-spacing: 0.5px;
  }
  .brand-tagline {
    left: 198px; top: 90px; margin: 0;
    font: 400 30px/1 var(--sans-head); color: #e6e6e6; letter-spacing: -0.3px;
  }
  .headline {
    left: 0; width: 700px; top: 147px; margin: 0; text-align: center;
    font: 700 31px/1 var(--sans-body); color: #e8e8e8;
  }

  /* Front: services */
  .service-list { list-style: none; margin: 0; padding: 0; }
  .service-item { position: absolute; left: 350px; display: flex; align-items: center; }
  .icon-badge {
    width: 68px; height: 68px; border-radius: 50%; box-sizing: border-box;
    background: var(--white); border: 3px solid var(--red);
    display: flex; align-items: center; justify-content: center; flex: none;
  }
  .icon-badge svg { width: 38px; height: 38px; fill: var(--ink); }
  .service-label {
    margin-left: 20px; font: 700 25px/30px var(--serif); color: var(--ink);
  }

  .call { left: 350px; top: 745px; display: flex; align-items: center; }
  .call-badge {
    width: 72px; height: 72px; border-radius: 50%; background: var(--black);
    display: flex; align-items: center; justify-content: center;
  }
  .call-badge svg { width: 42px; height: 42px; fill: none; stroke: var(--white); stroke-width: 1.6; }
  .call-text { margin-left: 18px; color: var(--ink); font-family: var(--serif); }
  .call-text .cta { display: block; font-weight: 600; font-size: 35px; line-height: 32px; }
  .call-text .phone { display: block; font-weight: 700; font-size: 45px; line-height: 44px; letter-spacing: -1px; }

  /* Front: offer badge */
  .offer-ring {
    left: 40px; top: 545px; width: 290px; height: 290px; border-radius: 50%;
    box-sizing: border-box; border: 3px solid #3a3a3a; background: rgba(0,0,0,0.15);
  }
  .offer {
    left: 52px; top: 557px; width: 266px; height: 266px; border-radius: 50%;
    background: var(--black); color: var(--white); text-align: center;
    font-family: var(--serif); box-sizing: border-box; padding-top: 52px;
  }
  .offer .big { display: block; font-weight: 700; font-size: 44px; line-height: 44px; }
  .offer .small { display: block; font-weight: 700; font-size: 20px; line-height: 24px; }
  .offer .rule { display: block; width: 62px; height: 2px; background: var(--white); margin: 18px auto 14px; }
  .offer .mid { display: block; font-weight: 700; font-size: 32px; line-height: 32px; }

  .address {
    left: 0; width: 700px; top: 910px; margin: 0; text-align: center;
    font: 400 17px/1 var(--sans-body); color: #d4d4d4;
  }
  .website {
    left: 0; width: 700px; top: 936px; margin: 0; text-align: center;
    font: 400 21px/1 var(--sans-body); color: #d4d4d4; letter-spacing: 3.6px;
  }

  /* Back: service rows */
  .photo { position: absolute; width: 261px; }
  .dot {
    position: absolute; width: 66px; height: 66px; border-radius: 50%; box-sizing: border-box;
    background: var(--red); border: 3px solid var(--white);
    display: flex; align-items: center; justify-content: center;
  }
  .dot svg { width: 36px; height: 36px; fill: var(--white); }
  .detail { position: absolute; width: 360px; }
  .detail--right { text-align: right; }
  .detail h2 {
    margin: 0 0 14px; font: 700 24px/1 var(--serif); color: #c9c9c9;
  }
  .detail p {
    margin: 0; font: 400 15.5px/20px var(--sans-body); color: var(--white);
  }
</style>
</head>
<body>
<svg width="0" height="0" style="position:absolute" aria-hidden="true">
  <defs>
    <symbol id="i-vacuum" viewBox="0 0 40 40">
      <path d="M14 4c4 0 6 3 6 6v14h-3V10c0-2-1-3-3-3s-3 1-3 3v4H8v-4c0-3 2-6 6-6z"/>
      <path d="M16 22h8l4 12H12z"/>
      <circle cx="13" cy="36" r="2.5"/><circle cx="27" cy="36" r="2.5"/>
    </symbol>
    <symbol id="i-chair" viewBox="0 0 40 40">
      <path d="M9 12c0-4 3-6 6-6h10c3 0 6 2 6 6v5H9z"/>
      <path d="M4 17a3 3 0 0 1 6 0v4h20v-4a3 3 0 0 1 6 0v11H4z"/>
      <rect x="7" y="29" width="3" height="5"/><rect x="30" y="29" width="3" height="5"/>
    </symbol>
    <symbol id="i-drape" viewBox="0 0 40 40">
      <rect x="4" y="8" width="9" height="10"/><rect x="15" y="8" width="9" height="10"/>
      <rect x="4" y="20" width="9" height="10"/><rect x="15" y="20" width="9" height="10"/>
      <path d="M26 6h10v28l-5-3-5 3z"/>
    </symbol>
    <symbol id="i-tile" viewBox="0 0 40 40">
      <path d="M20 4l15 8-15 8-15-8z M20 8.5L10.5 12 20 16.5 29.5 12z" fill-rule="evenodd"/>
      <path d="M20 20l15 8-15 8-15-8z M20 24.5L10.5 28 20 32.5 29.5 28z" fill-rule="evenodd"/>
    </symbol>
    <symbol id="i-stone" viewBox="0 0 40 40">
      <path d="M14 4l1.5 4.5L20 10l-4.5 1.5L14 16l-1.5-4.5L8 10l4.5-1.5z"/>
      <path d="M28 8l1 3 3 1-3 1-1 3-1-3-3-1 3-1z"/>
      <path d="M12 20h16l3 6H9z"/><path d="M8 28h24l4 8H4z"/>
    </symbol>
  </defs>
</svg>

<main class="canvas">

  <!-- Front page -->
  <section class="page page--front">
    <svg class="fill" viewBox="0 0 700 990" preserveAspectRatio="none" aria-hidden="true">
      <defs>
        <linearGradient id="hero" x1="0" y1="0" x2="1" y2="0.3">
          <stop offset="0" stop-color="#4a4f52"/>
          <stop offset="0.45" stop-color="#9fa3a6"/>
          <stop offset="0.75" stop-color="#eceae9"/>
          <stop offset="1" stop-color="#d9c9c8"/>
        </linearGradient>
      </defs>
      <rect x="0" y="190" width="700" height="760" fill="url(#hero)"/>
      <path d="M0 198 Q330 275 700 195 V240 Q330 285 0 232 Z" fill="var(--red)"/>
      <path d="M0 0 H700 V195 Q330 262 0 200 Z" fill="var(--black)"/>
      <path d="M0 922 Q330 830 700 875 V990 H0 Z" fill="var(--red)"/>
      <path d="M0 940 Q350 880 700 935 V990 H0 Z" fill="var(--black)"/>
    </svg>
    <div class="abs" role="img" aria-label="Photo of a wet-extraction carpet cleaning machine with a clear ribbed hose" style="left:0;top:245px;width:700px;height:640px"></div>

    <span class="abs brand-dot" aria-hidden="true"></span>
    <h1 class="abs brand-name">MERIDIAN SWIFT</h1>
    <p class="abs brand-tagline">THE ART OF FINE RUG WASHING</p>
    <p class="abs headline">One Stop For All Your Home Cleaning Needs</p>

    <ul class="service-list">
      <li class="service-item" style="top:314px"><span class="icon-badge"><svg><use href="#i-vacuum"/></svg></span><span class="service-label">Carpet Cleaning</span></li>
      <li class="service-item" style="top:394px"><span class="icon-badge"><svg><use href="#i-chair"/></svg></span><span class="service-label">Upholstery Cleaning</span></li>
      <li class="service-item" style="top:478px"><span class="icon-badge"><svg><use href="#i-drape"/></svg></span><span class="service-label">Drapery Cleaning</span></li>
      <li class="service-item" style="top:561px"><span class="icon-badge"><svg><use href="#i-tile"/></svg></span><span class="service-label">Tile &amp; Grout Cleaning</span></li>
      <li class="service-item" style="top:644px"><span class="icon-badge"><svg><use href="#i-stone"/></svg></span><span class="service-label">Natural Stone<br>Cleaning &amp; Polishing</span></li>
    </ul>

    <div class="abs call">
      <span class="call-badge"><svg viewBox="0 0 40 40"><path d="M12 7l5 6-3 3c1 4 5 8 9 9l3-3 6 5-3 5c-10 0-20-10-20-20z"/><path d="M24 9a8 8 0 0 1 7 7M24 4a13 13 0 0 1 12 12"/></svg></span>
      <span class="call-text"><span class="cta">CALL NOW</span><span class="phone">702-555-0147</span></span>
    </div>

    <div class="abs offer-ring" aria-hidden="true"></div>
    <div class="abs offer">
      <span class="big">30 DAYS</span>
      <span class="small">SPECIAL OFFER</span>
      <span class="rule"></span>
      <span class="mid">DISCOUNT</span>
      <span class="small">ON NEXT SERVICE!</span>
    </div>

    <p class="abs address">4180 W. Crestline Avenue, Suite C, Las Vegas, Nevada 89102</p>
    <p class="abs website">www.meridianswiftrugcare.com</p>
  </section>

  <!-- Back page -->
  <section class="page page--back">
    <div class="photo" role="img" aria-label="Photo of a carpet extraction wand cleaning beige carpet" style="left:0;top:0;height:190px;background:linear-gradient(135deg,#d8c09a,#b89a70 60%,#cdb48c)"></div>
    <div class="dot" style="left:254px;top:27px"><svg><use href="#i-vacuum"/></svg></div>
    <div class="detail" style="left:316px;top:46px">
      <h2>Carpet Cleaning</h2>
      <p>Don't let dirty carpets spoil the look of your beautiful home. Our service with 37 years of cleaning carpets experience you can expect your carpets to look like new in most cases.</p>
    </div>

    <div class="photo" role="img" aria-label="Photo of a grey sofa with teal, grey and magenta cushions" style="left:439px;top:190px;height:205px;background:linear-gradient(160deg,#eeeeee,#b9b9b9 55%,#d6d6d6)"></div>
    <div class="dot" style="left:407px;top:220px"><svg><use href="#i-chair"/></svg></div>
    <div class="detail detail--right" style="left:23px;top:236px">
      <h2>Upholstery Cleaning</h2>
      <p>Every day use leaves your sofa's and chairs looking dingy and can smell like dog. Our dry cleaning, shampoo or rinse extraction will leave the fabric feel like clean sheet.</p>
    </div>

    <div class="photo" role="img" aria-label="Photo of dark grey curtains hanging on a rod over sheer white drapes" style="left:0;top:395px;height:203px;background:linear-gradient(90deg,#f2f2f2,#3a3b3d 25%,#5a5b5e 50%,#2e2f31 75%,#e6e6e6)"></div>
    <div class="dot" style="left:254px;top:420px"><svg><use href="#i-drape"/></svg></div>
    <div class="detail" style="left:316px;top:440px">
      <h2>Drapery Cleaning</h2>
      <p>Drapery's act like a filter attracting atmospheric soil that making them look dingy. We make it easy to dry clean in-home. It's safe and effective solutions and you get beautiful drapery again.</p>
    </div>

    <div class="photo" role="img" aria-label="Photo of a floor scrubbing machine cleaning a foamy tile floor" style="left:439px;top:597px;height:203px;background:linear-gradient(200deg,#9a9a9a,#d8d6d2 40%,#f1efeb)"></div>
    <div class="dot" style="left:407px;top:622px"><svg><use href="#i-tile"/></svg></div>
    <div class="detail detail--right" style="left:23px;top:641px">
      <h2>Tile &amp; Grout Cleaning</h2>
      <p>Tile and grout get neglected, dirty grout leave permanent staining. Let our professionals bring back the look of a new floor.</p>
    </div>

    <div class="photo" role="img" aria-label="Photo of a polished terrazzo stone floor in a bright dining room" style="left:0;top:800px;height:190px;background:linear-gradient(180deg,#c7cdd0,#8e969a 45%,#5c6367)"></div>
    <div class="dot" style="left:254px;top:820px"><svg><use href="#i-stone"/></svg></div>
    <div class="detail" style="left:316px;top:840px">
      <h2>Natural Stone Cleaning &amp; Polishing</h2>
      <p>A dull stained marble - granite - travertine and other natural stone can be revitalized to look bew again.</p>
    </div>
  </section>

</main>
</body>
</html>
```